Building company requiring web site design

We need a web design for a new company based in Sydney called Kestrel Building Co. We build and renovate new and existing homes for consumers. We would like to see design that use the colours red and grey. The final design should communicate innovative building but with old fashion quality, great customer service and attention to detail. I have already had a logo and stationary design completed and would like to use the these colour schemes
Updates

Target Market(s)

Home owners, investors

Industry/Entity Type

Building

Coding

Coded - Design and coding required

Number of Pages Required

5+ page

Requirements
Must have
• Home page, contact page, about us page, gallery page and testimonial page
Nice to have
• Contact form

```html
<!DOCTYPE html>
<html lang="en">
<head>
<meta charset="utf-8">
<title>Kestrel Building Co.</title>
<link rel="stylesheet" href="https://fonts.googleapis.com/css2?family=Bitter:wght@400;700&family=Open+Sans:wght@400;600;700&family=PT+Sans:wght@400;700&family=Montserrat:wght@600&display=swap">
<style>
:root{
  --red:#b5413f;
  --red-text:#b03a38;
  --dark:#333333;
  --ink:#2b2b2b;
  --body:#444444;
  --band:#e4e4e4;
  --footer:#141414;
  --footer-base:#232323;
  --footer-text:#b8a77a;
  --footer-muted:#9a9a9a;
  --white:#ffffff;
}
*{box-sizing:border-box;margin:0;padding:0}
html,body{width:1200px;height:2493px;overflow:hidden;background:var(--white)}
body{position:relative;font-family:"PT Sans",sans-serif;color:var(--body)}
.abs{position:absolute}
.top-rule{left:0;top:0;width:1200px;height:7px;background:var(--ink)}
.brand{left:60px;top:58px;font-family:"Bitter",serif;font-weight:700;font-size:30px;color:var(--red);display:flex;align-items:center;gap:12px}
.brand-square{width:22px;height:22px;background:var(--red)}
.contact-pill{top:64px;height:62px;border-radius:31px;background:linear-gradient(#f6f6f6,#e9e9e9);padding:6px 0 0 66px;font-family:"Open Sans",sans-serif}
.contact-pill small{display:block;font-size:15px;color:#555;margin-left:6px}
.contact-pill strong{display:block;font-size:21px;color:var(--ink);font-weight:600}
.contact-pill svg{position:absolute;left:22px;top:26px}
.pill-call{left:585px;width:240px}
.pill-mail{left:832px;width:290px}
.main-nav{left:60px;top:158px;width:1080px;height:48px;background:var(--red);border-radius:3px;display:flex;overflow:hidden}
.main-nav a{font-family:"Open Sans",sans-serif;font-size:16px;font-weight:600;color:var(--white);text-decoration:none;line-height:48px;padding:0 31px}
.main-nav a.current{background:var(--dark);padding:0 33px}
.hero{left:0;top:208px;width:1200px;height:515px;background:linear-gradient(110deg,#6a4a34 0%,#8a7060 35%,#c9c6c2 60%,#3d4f78 85%,#2c3550 100%)}
.hero-arrow{top:384px;width:60px;height:60px;border-radius:50%;background:rgba(60,60,60,.75)}
.hero-caption{left:206px;top:605px;width:788px;height:86px;background:rgba(70,70,70,.85);color:var(--white);font-family:"Open Sans",sans-serif;font-size:26px;font-weight:600;text-align:center;line-height:34px;padding-top:10px;letter-spacing:.5px}
.welcome-title{left:60px;top:780px;font-family:"Bitter",serif;font-size:33px;color:var(--ink)}
.welcome-text{left:65px;top:832px;width:715px;font-size:15.5px;line-height:24px}
.welcome-text p+p{margin-top:24px}
.read-more{left:65px;top:1002px;font-size:14px;font-weight:700;color:var(--red-text)}
.welcome-photo{left:813px;top:806px;width:326px;height:200px;background:linear-gradient(#1f4a6a,#4d6b7a 55%,#b4763a 75%,#6a4a2a)}
.services{left:0;top:1100px;width:1200px;height:410px;background:var(--band)}
.service-title{top:1153px;font-family:"Bitter",serif;font-size:23px;font-weight:700;color:var(--ink);letter-spacing:.5px}
.service-title em{font-style:normal;color:var(--red-text)}
.service-frame{top:1206px;width:327px;height:194px;background:var(--white);padding:5px;box-shadow:0 0 3px rgba(0,0,0,.3)}
.service-frame div{width:100%;height:100%}
.pager{left:527px;top:1509px;width:137px;height:37px;background:var(--band);display:flex;justify-content:center;align-items:center;gap:14px}
.section-title{top:1624px;font-family:"Bitter",serif;font-size:24px;color:var(--ink);letter-spacing:.5px}
.project-photo{left:61px;top:1679px;width:307px;height:171px;background:linear-gradient(135deg,#d8d8d8,#a9b6c2 50%,#c9a23a 80%,#8c8c8c)}
.project-text{left:63px;top:1876px;width:315px;font-size:15px;line-height:22px}
.quote-mark{left:427px;top:1666px;font-family:"Bitter",serif;font-size:44px;color:#999;line-height:1}
.quote-text{left:427px;top:1683px;width:300px;font-size:15px;line-height:24px;text-indent:38px}
.quote-name{left:500px;top:1880px;width:150px;text-align:right;font-size:15px;color:var(--red-text)}
.quote-role{left:430px;top:1905px;width:220px;text-align:right;font-size:15px}
.quote-avatar{left:662px;top:1868px;width:66px;height:63px;background:linear-gradient(#b58b6e,#4a3a30)}
.gallery-arrows{left:1080px;top:1630px;display:flex;gap:14px}
.gallery-main{left:793px;top:1679px;width:340px;height:201px;background:linear-gradient(110deg,#6a4a34,#c9c6c2 55%,#3d4f78)}
.gallery-thumb{top:1898px;width:76px;height:37px}
.skyline{left:0;top:2052px;width:1200px;height:76px;background:linear-gradient(#ffffff 0%,#ffffff 30%,#111 30%)}
.footer{left:0;top:2127px;width:1200px;height:308px;background:var(--footer)}
.footer-head{top:2201px;font-family:"Montserrat",sans-serif;font-size:13px;font-weight:600;color:var(--white);letter-spacing:.3px}
.footer-text{font-size:11.5px;line-height:20px;color:var(--footer-text)}
.footer-links a{position:absolute;font-size:11.5px;color:var(--white);text-decoration:none}
.office-row{left:607px;display:flex;gap:20px;font-size:11.5px;color:var(--footer-text);line-height:20px}
.office-row svg{flex:none;margin-top:3px}
.hours-row{left:880px;width:228px;display:flex;justify-content:space-between;font-size:11.5px;color:var(--footer-muted);border-bottom:1px solid #2a2a2a;padding-bottom:8px}
.hours-row b{color:var(--white);font-weight:700}
.copyright{left:0;top:2435px;width:1200px;height:58px;background:var(--footer-base);color:#777;font-size:14px;text-align:center;line-height:58px}
</style>
</head>
<body>
<div class="abs top-rule"></div>

<header>
  <div class="abs brand"><span class="brand-square"></span>Kestrel Building Co.</div>
  <div class="abs contact-pill pill-call">
    <svg width="22" height="22" viewBox="0 0 24 24"><path fill="#777" d="M6.6 10.8a15 15 0 0 0 6.6 6.6l2.2-2.2c.3-.3.7-.4 1-.2 1.1.4 2.3.6 3.6.6.6 0 1 .4 1 1V20c0 .6-.4 1-1 1A17 17 0 0 1 3 4c0-.6.4-1 1-1h3.5c.6 0 1 .4 1 1 0 1.3.2 2.5.6 3.6.1.3 0 .7-.2 1z"/></svg>
    <small>(Call us)</small><strong>+1800-555-20417</strong>
  </div>
  <div class="abs contact-pill pill-mail">
    <svg width="22" height="18" viewBox="0 0 24 18"><rect x="1" y="1" width="22" height="16" rx="2" fill="#888"/><path d="M2 2l10 8 10-8" stroke="#eee" stroke-width="1.6" fill="none"/></svg>
    <small>(E-mail)</small><strong>info@kestrelbuilding.com</strong>
  </div>
  <nav class="abs main-nav">
    <a class="current" href="#">HOME</a><a href="#">FEATURES</a><a href="#">SERVICES</a><a href="#">PROJECTS</a><a href="#">NEWS</a><a href="#">SHOP</a><a href="#">CAREER</a><a href="#">CONTACT</a>
  </nav>
</header>

<section>
  <div class="abs hero" role="img" aria-label="Builders in hard hats reviewing a large set of plans together"></div>
  <div class="abs hero-arrow" style="left:13px"><svg width="60" height="60"><path d="M34 20l-10 10 10 10" stroke="#fff" stroke-width="3" fill="none"/></svg></div>
  <div class="abs hero-arrow" style="left:1127px"><svg width="60" height="60"><path d="M26 20l10 10-10 10" stroke="#fff" stroke-width="3" fill="none"/></svg></div>
  <div class="abs hero-caption">LOOKING FOR A QUALITY CONSTRUCTOR<br>FOR YOUR NEXT PROJECT?</div>
</section>

<section>
  <h1 class="abs welcome-title" style="font-weight:400">Welcome to Kestrel Building Co.</h1>
  <div class="abs welcome-text">
    <p>We will assign a project manager, field superintendent, engineer and other staff members as required to effectively manage the construction process. Praesent dapibus, neque id cursus faucibus, tortor neque egestas augue, eu vulputate magna eros eu erat. Aliquam erat volutpat. Nam dui mi, tincidunt quis, accumsan porttitor, facilisis luctus, metus.</p>
    <p>During the construction of any project, the coordination of the trades is an integral part of the process, especially with respect to the mechanical and electrical trades.</p>
  </div>
  <a class="abs read-more">Read More ››</a>
  <div class="abs welcome-photo" role="img" aria-label="Orange excavator on a building site at dusk"></div>
</section>

<section>
  <div class="abs services"></div>
  <h2 class="abs service-title" style="left:63px"><em>BEST HOUSE</em> RENOVATION</h2>
  <h2 class="abs service-title" style="left:427px"><em>THE EFFECTIVE</em> TEAMWORK</h2>
  <h2 class="abs service-title" style="left:793px"><em>KESTREL</em> BUILDING</h2>
  <div class="abs service-frame" style="left:65px"><div role="img" aria-label="Two renovation workers in yellow hard hats" style="background:linear-gradient(#d9c9a8,#8f7a5a)"></div></div>
  <div class="abs service-frame" style="left:428px"><div role="img" aria-label="Engineers with plans on a site under a crane" style="background:linear-gradient(#5d86c0,#b8c8da 60%,#7a7a70)"></div></div>
  <div class="abs service-frame" style="left:793px"><div role="img" aria-label="Workers laying laminate flooring" style="background:linear-gradient(#e8e4de,#b59a7a)"></div></div>
  <div class="abs pager">
    <svg width="12" height="18"><path d="M10 2L3 9l7 7" stroke="#b03a38" stroke-width="2.5" fill="none"/></svg>
    <svg width="12" height="18"><path d="M2 2l7 7-7 7" stroke="#b03a38" stroke-width="2.5" fill="none"/></svg>
  </div>
</section>

<section>
  <h2 class="abs section-title" style="left:61px;font-weight:400">KESTREL PROJECT</h2>
  <div class="abs project-photo" role="img" aria-label="Builders in hard hats studying a blueprint"></div>
  <p class="abs project-text">Constructor explains how you can enjoy high end flooring trends like textured wood and realistic stones with new laminate flooring.</p>

  <h2 class="abs section-title" style="left:426px;font-weight:400">TESTIMONIALS</h2>
  <div class="abs quote-mark">“</div>
  <p class="abs quote-text">simply dummy text of the printing and typesetting industry. Lorem Ipsum has been the industry's standard dummy text ever since the 1500s, when an unknown printer took a galley of type and scrambled it to make when an unknown printer &nbsp;a type specimen book.</p>
  <div class="abs quote-name">-Mark Ellison</div>
  <div class="abs quote-role">It was popularised 1960s</div>
  <div class="abs quote-avatar" role="img" aria-label="Portrait of the client"></div>

  <h2 class="abs section-title" style="left:791px;font-weight:400">GALLERY</h2>
  <div class="abs gallery-arrows">
    <svg width="12" height="18"><path d="M10 2L3 9l7 7" stroke="#b03a38" stroke-width="2.5" fill="none"/></svg>
    <svg width="12" height="18"><path d="M2 2l7 7-7 7" stroke="#b03a38" stroke-width="2.5" fill="none"/></svg>
  </div>
  <div class="abs gallery-main" role="img" aria-label="Builders reviewing plans on site"></div>
  <div class="abs gallery-thumb" style="left:793px;background:linear-gradient(#3b5a78,#c06a2a)" role="img" aria-label="Excavator thumbnail"></div>
  <div class="abs gallery-thumb" style="left:880px;background:linear-gradient(#ddd,#4a6aa8)" role="img" aria-label="Flooring work thumbnail"></div>
  <div class="abs gallery-thumb" style="left:967px;background:linear-gradient(#c9b08a,#b04040)" role="img" aria-label="Workers thumbnail"></div>
  <div class="abs gallery-thumb" style="left:1054px;background:linear-gradient(#3a2a20,#a06a40)" role="img" aria-label="Interior work thumbnail"></div>
</section>

<footer>
  <div class="abs skyline" role="img" aria-label="Black city skyline silhouette"></div>
  <div class="abs footer"></div>

  <h3 class="abs footer-head" style="left:63px">ABOUT COMPANY</h3>
  <p class="abs footer-text" style="left:63px;top:2240px;width:230px">Our clients range from blue-chip companies, to large organisations and some small local businesses who are striving to expand.</p>
  <p class="abs footer-text" style="left:63px;top:2316px;width:230px">To see a detailed list of our works and the progress please see our project page.</p>

  <h3 class="abs footer-head" style="left:336px">COMPANY</h3>
  <div class="footer-links">
    <a style="left:336px;top:2244px">Home</a><a style="left:451px;top:2244px">Who We Are</a>
    <a style="left:336px;top:2280px">Company News</a><a style="left:451px;top:2280px">Our Services</a>
    <a style="left:336px;top:2316px">Projects</a><a style="left:451px;top:2316px">Shop</a>
    <a style="left:336px;top:2352px">Careers</a><a style="left:451px;top:2352px">Contact Us</a>
  </div>

  <h3 class="abs footer-head" style="left:608px">CONSTRUCTION OFFICE</h3>
  <div class="abs office-row" style="top:2240px"><svg width="10" height="14"><path d="M5 0a5 5 0 0 1 5 5c0 4-5 9-5 9S0 9 0 5a5 5 0 0 1 5-5z" fill="#888"/></svg><span>42 Harbour Lane<br>Pyrmont NSW 2009</span></div>
  <div class="abs office-row" style="top:2296px"><svg width="11" height="11" viewBox="0 0 24 24"><path fill="#888" d="M6.6 10.8a15 15 0 0 0 6.6 6.6l2.2-2.2c.3-.3.7-.4 1-.2 1.1.4 2.3.6 3.6.6.6 0 1 .4 1 1V20c0 .6-.4 1-1 1A17 17 0 0 1 3 4c0-.6.4-1 1-1h3.5c.6 0 1 .4 1 1 0 1.3.2 2.5.6 3.6.1.3 0 .7-.2 1z"/></svg><span>1.800.555.204</span></div>
  <div class="abs office-row" style="top:2324px"><svg width="11" height="9"><rect width="11" height="9" fill="#888"/></svg><span style="color:#fff">office@kestrelbuilding.com</span></div>
  <div class="abs office-row" style="top:2352px"><svg width="11" height="11"><rect width="11" height="11" rx="1" fill="#888"/></svg><span>FAX: (02) 5550-1839</span></div>

  <h3 class="abs footer-head" style="left:880px">BUSINESS HOURS</h3>
  <p class="abs footer-text" style="left:880px;top:2240px;width:230px">Our support available to help you 24 hours a day, seven days a week.</p>
  <div class="abs hours-row" style="top:2304px"><span>Monday-Friday:</span><b>9am to 5pm</b></div>
  <div class="abs hours-row" style="top:2338px"><span>Saturday:</span><b>10am to 2pm</b></div>
  <div class="abs hours-row" style="top:2372px;border:none"><span>Sunday:</span><b>Closed</b></div>

  <div class="abs copyright">Copyright © 2016 Kestrel Building Co. All Right Revered.</div>
</footer>
</body>
</html>
```